Hip / Cool Business Card for Custom Accessory Company

I would like to get a 2 sided design for standard size business cards, glossy (2 inches x 3.5 inches). Can be landscape or portrait layout! The design should include our logo (attached). The card should be extremely clear that the company is Tin Lantern. Should also have our URL clear. Should also use the color scheme seen on our upcoming site, tinlantern-example.com. The font we use is called "hurry up." Other than that, please go-to-town. We are targeting 15-45 y.o. market, with a skew on the 20-30 crowd. We do custom and stock iPhone cases as well as Cufflinks, Winestoppers; see the website for more.
Updates

Project Deadline Extended
Reason: Extending in case the US July 4th Holiday is keeping people from working!!

Industry/Entity Type

Landscape

Requirements
Must have
• Must be clear that the website is tinlantern-example.com. Must be clear that custom designs are an option.
Nice to have
• images of our designs. examples of our designs.
Should not have
• hard on the eyes contrasting colors such as orange on black. green on blue. Should not have any fonts that are considered "old" like Times New Roman. But decorative fonts are fine.

```html
<!DOCTYPE html>
<html lang="en">
<head>
<meta charset="utf-8">
<title>Tin Lantern – Business Card</title>
<link href="https://fonts.googleapis.com/css2?family=Arimo:wght@400;700&display=swap" rel="stylesheet">
<style>
  :root {
    --teal: #23a0a8;
    --teal-deep: #1b8a91;
    --ink: #1a1a1a;
    --text: #2a2a2a;
    --paper: #ffffff;
    --backdrop: #e9e7e4;
  }
  html, body {
    margin: 0;
    width: 1200px;
    height: 1016px;
    overflow: hidden;
    background: var(--backdrop);
    font-family: "Arimo", Arial, sans-serif;
  }
  .card {
    position: absolute;
    top: 68px;
    width: 491px;
    height: 854px;
    border-radius: 33px;
    overflow: hidden;
    box-shadow: 0 6px 18px rgba(0,0,0,0.18);
  }
  .card--front { left: 72px; background: var(--paper); }
  .card--back { left: 648px; background: var(--teal); }

  .brand {
    position: absolute;
    display: flex;
    flex-direction: column;
    align-items: center;
    gap: 14px;
  }
  .brand__dot {
    width: 120px;
    height: 120px;
    border-radius: 50%;
  }
  .brand__name {
    font-weight: 700;
    font-size: 38px;
    letter-spacing: 1px;
    text-transform: uppercase;
    white-space: nowrap;
  }
  .card--front .brand { left: 28px; top: 30px; width: 250px; }
  .card--front .brand__dot { background: var(--teal); }
  .card--front .brand__name { color: var(--ink); }

  .card--back .brand { left: 0; right: 0; top: 260px; }
  .card--back .brand__dot { background: var(--teal-deep); }
  .card--back .brand__name { color: var(--paper); }

  .person {
    position: absolute;
    right: 33px;
    top: 432px;
    font-size: 24px;
    font-weight: 700;
    color: var(--ink);
  }
  .person__title { font-size: 17px; font-weight: 400; }

  .contacts {
    position: absolute;
    right: 33px;
    top: 506px;
    margin: 0;
    padding: 0;
    list-style: none;
    text-align: right;
    font-size: 21px;
    color: var(--text);
  }
  .contacts li {
    display: flex;
    justify-content: flex-end;
    align-items: center;
    gap: 8px;
    height: 34.5px;
    white-space: nowrap;
  }
  .contacts svg { width: 18px; height: 18px; fill: var(--teal); flex: none; }

  .band { position: absolute; left: 0; top: 0; width: 491px; height: 854px; }

  .address {
    position: absolute;
    right: 33px;
    top: 755px;
    text-align: right;
    color: var(--paper);
    font-size: 22px;
    line-height: 31px;
    white-space: nowrap;
  }

  .site {
    position: absolute;
    left: 0; right: 0;
    top: 554px;
    text-align: center;
    color: var(--paper);
    font-size: 33px;
    letter-spacing: 0.5px;
    white-space: nowrap;
  }
  .offer {
    position: absolute;
    left: 0; right: 0;
    top: 612px;
    text-align: center;
    color: var(--paper);
    font-size: 21px;
    white-space: nowrap;
  }
</style>
</head>
<body>

<section class="card card--front">
  <div class="brand">
    <div class="brand__dot"></div>
    <div class="brand__name">Tin Lantern</div>
  </div>

  <div class="person">Your Name <span class="person__title">Title</span></div>

  <ul class="contacts">
    <li>
      <svg viewBox="0 0 20 20" aria-hidden="true"><path d="M3 8c0-2 3-4 7-4s7 2 7 4v2h-4V8H7v2H3z"/><rect x="4" y="11" width="12" height="7" rx="1"/></svg>
      555-014-2287
    </li>
    <li>
      <svg viewBox="0 0 20 20" aria-hidden="true"><rect x="5" y="2" width="10" height="6"/><rect x="2" y="8" width="16" height="7" rx="1"/><rect x="5" y="13" width="10" height="5"/></svg>
      555-014-2287
    </li>
    <li>
      <svg viewBox="0 0 20 20" aria-hidden="true"><circle cx="10" cy="10" r="8"/><path d="M2 10h16M10 2c-3 3-3 13 0 16M10 2c3 3 3 13 0 16" stroke="#fff" stroke-width="1.2" fill="none"/></svg>
      www.tinlantern-example.com
    </li>
    <li>
      <svg viewBox="0 0 20 20" aria-hidden="true"><path d="M2 8l8-5 8 5v9H2z"/><path d="M2 8l8 5 8-5" fill="#fff" opacity=".6"/></svg>
      support@tinlantern-example.com
    </li>
  </ul>

  <svg class="band" viewBox="0 0 491 854" aria-hidden="true">
    <path d="M0 735 Q245 668 491 725 L491 854 L0 854 Z" fill="var(--teal)"/>
    <path d="M0 714 Q245 648 491 706" fill="none" stroke="var(--ink)" stroke-width="5"/>
  </svg>

  <div class="address">418B Cedar Brook<br>Lane Suite 207, Fairlawn, OH 44333</div>
</section>

<section class="card card--back">
  <div class="brand">
    <div class="brand__dot"></div>
    <div class="brand__name">Tin Lantern</div>
  </div>
  <div class="site">www.tinlantern-example.com</div>
  <div class="offer">Custom designs available</div>
</section>

</body>
</html>
```